Brevora Ad Image Design Competition

We're seeking creative designers to develop a series of engaging Brevora advertisements for Moltcraft with original art work.

The goal is to create scroll-stopping ads that capture attention through humor, nostalgia, and compelling storytelling while maintaining professional appeal.

Creative Brief:
Please read the "Core Messages to Convey"
https://pages.quillbarn.net/sheet/p/7kRtw2QmLv9xNcBe4HjYa63-s08ZueTFd_q51hnWpZ3/view?tab=t.0#heading=h.4mrwtzcja2k

Target Market(s)

Busy executives focusing on making their company more efficient

Requirements
Must have
• An image ( not copy) that speaks to one of our "Core Messages to Convey"

```html
<!DOCTYPE html>
<html lang="en">
<head>
<meta charset="utf-8">
<title>Moltcraft – Streamline Disparate Systems</title>
<link rel="stylesheet" href="https://fonts.googleapis.com/css2?family=Poppins:wght@400;600;700;800&display=swap">
<style>
  :root {
    --cream: #f9f8ee;
    --navy: #2d2940;
    --ink: #26233a;
    --red: #d52a2a;
    --white: #ffffff;
    --art-teal: #a9e6e6;
    --art-slate: #4f6a82;
    --art-gold: #f6c02e;
  }
  * { margin: 0; padding: 0; box-sizing: border-box; }
  html, body { width: 1200px; height: 1200px; overflow: hidden; background: var(--cream); }
  .ad {
    position: relative;
    width: 1200px;
    height: 1200px;
    font-family: "Poppins", sans-serif;
    overflow: hidden;
  }
  .hero {
    position: absolute;
    inset: 0 0 auto 0;
    height: 773px;
    background: var(--cream);
  }
  .brand {
    position: absolute;
    left: 96px;
    top: 92px;
    display: flex;
    align-items: center;
    gap: 22px;
    font-weight: 600;
    font-size: 64px;
    color: var(--ink);
    letter-spacing: -0.5px;
  }
  .brand-dot {
    width: 58px;
    height: 58px;
    border-radius: 50%;
    background: var(--ink);
  }
  .hero-art {
    position: absolute;
    left: 340px;
    top: 36px;
    width: 860px;
    height: 740px;
  }
  .headline {
    position: absolute;
    left: 74px;
    top: 274px;
    font-weight: 800;
    font-size: 106px;
    line-height: 95px;
    letter-spacing: -1px;
    text-transform: uppercase;
  }
  .headline .accent { color: var(--red); display: block; }
  .headline .strong { color: var(--ink); display: block; }
  .benefit {
    position: absolute;
    inset: 773px 0 0 0;
    background: var(--navy);
  }
  .benefit-icon {
    position: absolute;
    left: 144px;
    top: 856px;
    width: 194px;
    height: 234px;
  }
  .benefit-title {
    position: absolute;
    left: 400px;
    top: 846px;
    font-weight: 800;
    font-size: 58px;
    line-height: 62px;
    color: var(--red);
    letter-spacing: 0.3px;
  }
  .benefit-text {
    position: absolute;
    left: 400px;
    top: 980px;
    font-weight: 400;
    font-size: 49px;
    line-height: 64px;
    color: var(--white);
  }
</style>
</head>
<body>
<main class="ad">
  <section class="hero">
    <div class="brand"><span class="brand-dot"></span>Moltcraft</div>

    <svg class="hero-art" viewBox="0 0 860 740" role="img" aria-label="Illustration of business people climbing a rising staircase of bars toward a large upward arrow topped with a glowing light bulb">
      <defs>
        <linearGradient id="artFill" x1="0" y1="1" x2="1" y2="0">
          <stop offset="0" stop-color="#bfeeea"/>
          <stop offset="0.55" stop-color="#7fa6b8"/>
          <stop offset="1" stop-color="#3f5670"/>
        </linearGradient>
      </defs>
      <path d="M140 740 L140 560 L400 560 L400 330 L600 330 L600 60 L820 60 L820 740 Z" fill="url(#artFill)" opacity="0.9"/>
    </svg>

    <h1 class="headline">
      <span class="accent">Streamline</span>
      <span class="accent">Disparate</span>
      <span class="strong">Systems</span>
    </h1>
  </section>

  <section class="benefit">
  </section>

  <svg class="benefit-icon" viewBox="0 0 194 234" fill="none" stroke="#f5f3ea" stroke-width="7" stroke-linecap="round" stroke-linejoin="round" aria-hidden="true">
    <circle cx="118" cy="157" r="70"/>
    <circle cx="118" cy="157" r="50" stroke-dasharray="22 12"/>
    <circle cx="118" cy="157" r="11"/>
    <path d="M126 149 L160 112"/>
    <circle cx="50" cy="100" r="46" fill="#2d2940"/>
    <path d="M58 70 L38 104 L56 104 L44 132 L70 96 L52 96 Z"/>
    <path d="M120 80 V10 M100 30 L120 8 L140 30"/>
    <path d="M150 80 V52 M136 66 L150 48 L164 66"/>
    <path d="M176 100 V72 M164 84 L176 68 L188 84"/>
  </svg>

  <h2 class="benefit-title">Accelerated Value<br>Creation</h2>
  <p class="benefit-text">Accelerate your value<br>creation journey</p>
</main>
</body>
</html>
```